Zielgruppe
Wir sind ein Vertriebsunternehmen, mit dem Ziel die klassische Finanz und den Kryptosektor zu verbinden. Unsere Zielgruppe sind Menschen zwischn 25 - 45 Jahre. Wir sind die Communty und Vertrieb der ersten rechtkonformen STO - Plattform ( Plattform für Wertpapiere im Kryptosektor)
Diese Projekt ist Teil eines Paketes, wir bitten nur Designer mit zu machen die alle benötigten Unterlagen designen können. (siehe restliche Projekte) - Gesamtvolumen: 2300€ Preisgeld
Online-Marketing Material
2 Vorlagen Social Media - (Einladung/Event, Sprüche/Information)
Banner
Präsentationsvorlagen - min unterschiedliche 8 Vorlagenseiten /Layouts.
Landingpage Layout f. Funnelsite für Webinaranmeldung mit Platz für Formular
Newsletter Layoutvorlage
Vorlage Infografik
Broschüre / E - Book Designe
Es werden nur Vorlagen benötigt mit 'LoremSum Texten' und Musterbildern. Wir möchten von allen Vorlagen die Originaldatei, uns stehen folgende Grafikprogramme zur Verfügung:
Adobe Photoshop
Adobe Illustrator
Canva
Newsletter und Landingpage Software: postflinkel.com
Unsere Akt. Designe (Designe Alt) gefällt uns von der Idee, dennoch wünschen wir es uns moderner und edler mit ein wenig 'spaceig'. - Eben die Vereinigung von Kryptowelt und klassischer Finanz.
Schriftart: Poppins
Farben lt. Logo
Aufgabenstellung
Diese Projekt ist Teil eines Paketes, wir bitten nur Designer mit zu machen die alle benötigten Unterlagen designen können. (siehe restliche Projekte) - Gesamtvolumen: 2000€ - 2300€ Preisgeld

```html
<!DOCTYPE html>
<html lang="de">
<head>
<meta charset="utf-8">
<title>Zitat-Vorlage – GreenKestrel Investments</title>
<link href="https://fonts.googleapis.com/css2?family=Raleway:ital,wght@0,500;0,700;1,300;1,400;1,500;1,700&display=swap" rel="stylesheet">
<style>
  :root {
    --brand-blue: #2a6db6;
    --brand-navy: #1f4f9c;
    --slate-light: #aab5c4;
    --slate-dark: #95a2b3;
    --frame-grey: #9aa6b6;
    --paper: #ffffff;
    --ink-soft: #5b6472;
  }
  html, body {
    margin: 0;
    padding: 0;
    width: 1200px;
    height: 1200px;
    overflow: hidden;
    background: var(--paper);
  }
  .quote-card {
    position: relative;
    width: 1200px;
    height: 1200px;
    font-family: "Raleway", sans-serif;
    background: var(--paper);
    overflow: hidden;
  }
  .card-shapes {
    position: absolute;
    inset: 0;
  }
  .quote-mark {
    position: absolute;
    left: 120px;
    top: 100px;
    font-family: "Raleway", sans-serif;
    font-weight: 700;
    font-style: italic;
    font-size: 210px;
    line-height: 1;
    color: var(--paper);
  }
  .quote-text {
    position: absolute;
    left: 228px;
    top: 146px;
    width: 790px;
    margin: 0;
    font-style: italic;
    font-weight: 500;
    font-size: 54px;
    line-height: 78px;
    color: var(--paper);
  }
  .author {
    position: absolute;
    left: 228px;
    top: 680px;
    color: var(--paper);
    font-style: italic;
  }
  .author-name {
    margin: 0;
    font-weight: 700;
    font-size: 34px;
    line-height: 40px;
  }
  .author-role {
    margin: 14px 0 0;
    font-weight: 300;
    font-size: 36px;
    line-height: 40px;
  }
  .brand {
    position: absolute;
    right: 61px;
    top: 1087px;
    display: flex;
    align-items: center;
    gap: 12px;
  }
  .brand-square {
    width: 46px;
    height: 46px;
    background: var(--brand-navy);
  }
  .brand-words {
    display: flex;
    flex-direction: column;
  }
  .brand-name {
    font-weight: 700;
    font-size: 27px;
    line-height: 30px;
    color: var(--brand-navy);
    letter-spacing: 0.2px;
  }
  .brand-tagline {
    font-weight: 500;
    font-size: 14.5px;
    line-height: 18px;
    letter-spacing: 2.2px;
    color: var(--ink-soft);
  }
</style>
</head>
<body>
<main class="quote-card">
  <svg class="card-shapes" width="1200" height="1200" viewBox="0 0 1200 1200" xmlns="http://www.w3.org/2000/svg">
    <defs>
      <linearGradient id="slate-fade" x1="0" y1="0" x2="1" y2="0">
        <stop offset="0" stop-color="var(--slate-light)"/>
        <stop offset="1" stop-color="var(--slate-dark)"/>
      </linearGradient>
      <linearGradient id="portrait-tones" x1="0" y1="0" x2="0" y2="1">
        <stop offset="0" stop-color="#5f7048"/>
        <stop offset="0.5" stop-color="#3c4634"/>
        <stop offset="1" stop-color="#1d222c"/>
      </linearGradient>
      <filter id="frame-shadow" x="-20%" y="-20%" width="140%" height="140%">
        <feDropShadow dx="0" dy="8" stdDeviation="8" flood-color="#000" flood-opacity="0.25"/>
      </filter>
    </defs>

    <path class="blue-field" fill="var(--brand-blue)"
      d="M0 0 H1200 V615 L1093 673 L970 605 Q957 598 944 605 L756 713 Q742 722 742 738 V880 L455 1032 Q441 1040 427 1032 L0 797 Z"/>

    <path class="slate-corner" fill="url(#slate-fade)"
      d="M0 1122 L193 1023 Q204 1017 215 1023 L534 1200 H0 Z"/>

    <g class="portrait-frame" filter="url(#frame-shadow)">
      <path fill="var(--frame-grey)"
        d="M957 630 L1147 737 V950 L957 1057 L767 950 V737 Z" stroke="var(--frame-grey)" stroke-width="18" stroke-linejoin="round"/>
    </g>
    <path class="portrait-photo" role="img" aria-label="Porträtfoto des Geschäftsführers im dunklen Anzug vor grünem Garten"
      fill="url(#portrait-tones)" stroke="url(#portrait-tones)" stroke-width="10" stroke-linejoin="round"
      d="M957 652 L1125 748 V940 L957 1036 L789 940 V748 Z"/>
  </svg>

  <div class="quote-mark" aria-hidden="true">“</div>
  <p class="quote-text">Lorem ipsum dolor sit amet, consectetur adipiscing elit, sed do eiusmod tempor incididunt ut labore et dolore magna aliqua. Ut enim ad minim veniam,</p>

  <div class="author">
    <p class="author-name">MATTHIAS OBERLIN</p>
    <p class="author-role">Geschäftsführer</p>
  </div>

  <div class="brand">
    <div class="brand-square" aria-hidden="true"></div>
    <div class="brand-words">
      <span class="brand-name">GREENKESTREL INVESTMENTS</span>
      <span class="brand-tagline">KLUG UND SICHER IN FIRMENWERTE ANLEGEN</span>
    </div>
  </div>
</main>
</body>
</html>
```